Derek Holloway Photographer

Display and sell photos. I am based in the South Coast NSW Australia.
I mainly do land scape and sea scapes and wild life. I will consider all request for photos shoots except weddings. I will also take people on photo shoots in the local area. After people purchase a photo I will organise prints and mail them out. My web page sould be secure so people can not download my photos with out payment. I would like to purchase a domain page .com. The premium $16.00 month looks good. I need to add and remove photos as required.

Target Market(s)

People who appreciate the local environment, People who would like to hang good quality natural photos in their homes or shops, motels, cafes or businesses. I will go to sporting events or family outings to photograph family members, rather then the standard family portrate.

I try to take a good photo and not use the computer I belive in takeing a good photo is the skill.

Industry/Entity Type

Domain

Font styles to use
Sans Serif

Colors

Designer to choose colors to be used in the design.

Requirements
Must have
• People must be able to see my work and not run off with it.
Clean display for all the family.

```html
<!DOCTYPE html>
<html lang="en">
<head>
<meta charset="utf-8">
<title>Derek Holloway Photographer</title>
<link href="https://fonts.googleapis.com/css2?family=Montserrat:wght@400;500;600;700&family=Oswald:wght@400&family=Roboto:wght@400&display=swap" rel="stylesheet">
<style>
:root{
  --ochre:#d99a1e;
  --ochre-dark:#b8641a;
  --wood:#6e6f6c;
  --red:#b5473f;
  --green:#6fb043;
  --blue:#1a8fd0;
  --ink:#333;
  --panel:#e6e4dc;
  --white:#fff;
}
*{margin:0;padding:0;box-sizing:border-box}
html,body{width:1200px;height:960px;overflow:hidden}
body{
  position:relative;
  font-family:'Roboto',Arial,sans-serif;
  background:
    linear-gradient(to bottom,transparent 786px,var(--wood) 786px),
    radial-gradient(ellipse at 50% 30%,#e7b030 0%,var(--ochre) 45%,var(--ochre-dark) 100%);
}
.abs{position:absolute}
.logo{left:190px;top:18px;color:var(--white);font-family:'Montserrat',sans-serif;font-weight:500;font-size:31px;line-height:32px;letter-spacing:-0.5px}
.top-login{left:798px;top:52px;color:var(--blue);font-family:'Montserrat',sans-serif;font-weight:600;font-size:10px;letter-spacing:0.5px}
.search{left:860px;top:42px;width:152px;height:30px;background:var(--white);border:1px solid #ccc}
.search-icon{left:1018px;top:48px}
.page{left:120px;top:105px;width:960px;height:855px;background:var(--white)}
.nav{left:0;top:0;width:960px;height:27px;background:var(--red);border-bottom:1px solid #e9b7b3}
.nav a{position:absolute;top:0;color:var(--white);text-decoration:none;font-family:'Montserrat',sans-serif;font-weight:500;font-size:12px;letter-spacing:1px;line-height:27px}
.hero{left:0;top:28px;width:960px;height:298px;background:linear-gradient(90deg,#b39c86 0%,#9a8668 35%,#80703e 65%,#766c32 100%)}
.hero-title{left:584px;top:58px;color:var(--white);font-family:'Montserrat',sans-serif;font-weight:600;font-size:30px;letter-spacing:1px;text-shadow:0 2px 10px rgba(0,0,0,.4)}
.btn{background:var(--green);color:var(--white);font-family:'Oswald',sans-serif;text-align:center;border-radius:2px}
.hero-btn{left:586px;top:105px;width:115px;height:38px;line-height:38px;font-size:16px}
.portrait{left:68px;top:357px;width:204px;height:166px;background:linear-gradient(135deg,#e6dfdb,#b9afaa)}
.welcome{left:292px;top:358px;width:360px}
.welcome h1{font-family:'Montserrat',sans-serif;font-weight:400;font-size:18px;line-height:22px;color:var(--ink)}
.welcome h2{margin-top:3px;font-family:'Montserrat',sans-serif;font-weight:500;font-size:12px;line-height:18px;color:var(--blue)}
.welcome p{margin-top:6px;font-size:9.6px;line-height:16px;color:#222;text-align:justify}
.divider{left:674px;top:353px;height:146px;border-left:1px dotted #777}
.login{left:698px;top:349px;width:240px;height:157px;background:var(--panel)}
.login h3{position:absolute;left:27px;top:14px;font-family:'Montserrat',sans-serif;font-weight:400;font-size:16px;color:var(--ink)}
.login label{position:absolute;left:24px;font-size:10px;line-height:12px;color:#222}
.login .field{position:absolute;left:84px;width:128px;height:21px;background:var(--white);border:1px solid #bbb}
.login-btn{left:86px;top:112px;width:63px;height:25px;line-height:25px;font-size:14px}
.photos-band{left:0;top:553px;width:960px;height:168px;background:var(--panel)}
.photos-title{left:0;top:572px;width:960px;text-align:center;font-family:'Montserrat',sans-serif;font-weight:700;font-size:17px;letter-spacing:0.5px;color:var(--green)}
.photos-rule{left:186px;top:604px;width:588px;border-top:1px dotted #555}
.thumb{top:623px;height:116px}
.thumb-nature{left:186px;width:175px;background:linear-gradient(160deg,#d9d0b4,#8f9a6a)}
.thumb-scene{left:395px;width:173px;background:linear-gradient(160deg,#8a7f8e,#c7865a)}
.thumb-wildlife{left:601px;width:171px;background:linear-gradient(160deg,#6fbf3a,#3f8f22)}
.thumb-label{top:752px;width:175px;text-align:center;font-family:'Montserrat',sans-serif;font-weight:700;font-size:13px;letter-spacing:0.5px;color:var(--green)}
.footer{left:0;top:803px;width:960px;height:52px;background:var(--red);color:var(--white);text-align:center;font-size:10px;line-height:52px;letter-spacing:0.3px}
</style>
</head>
<body>
<div class="abs logo">DEREK<br>HOLLOWAY</div>
<div class="abs top-login">LOGIN</div>
<div class="abs search"></div>
<svg class="abs search-icon" width="18" height="18" viewBox="0 0 18 18"><circle cx="7" cy="7" r="5.5" fill="none" stroke="#111" stroke-width="2.5"/><line x1="11" y1="11" x2="16" y2="16" stroke="#111" stroke-width="3" stroke-linecap="round"/></svg>

<div class="abs page">
  <nav class="abs nav">
    <a style="left:210px">HOME</a>
    <a style="left:275px">ABOUT</a>
    <a style="left:351px">PORTFOLIO</a>
    <a style="left:458px">PURCHASE</a>
    <a style="left:559px">TESTIMONIALS</a>
    <a style="left:686px">CONTACT</a>
  </nav>
  <div class="abs hero" role="img" aria-label="Featured wildlife photograph of a red bird perched on a branch"></div>
  <div class="abs hero-title">PHOTO DESCRIPTION</div>
  <div class="abs btn hero-btn">LEARN MORE</div>

  <div class="abs portrait" role="img" aria-label="Photographer holding a camera"></div>
  <div class="abs welcome">
    <h1>Welcome to my site</h1>
    <h2>Lorem ipsum dolor sit amet, consectetuer adipiscing<br>elit, sed diam nonummy</h2>
    <p>nibh euismod tincidunt ut laoreet dolore magna aliquam erat volutpat. Ut wisi enim ad minim veniam, quis nostrud exerci tation ullamcorper suscipit lobortis nisl ut aliquip ex ea commodo consequat. Duis autem vel eum iriure dolor in hendrerit in vulputate velit esse molestie consequat, vel illum dolore eu feugiat nulla facilisis at vero eros et accumsan et iusto odio dignissim qui blandit praesent luptatum zzril delenit augue duis dolore</p>
  </div>
  <div class="abs divider"></div>
  <div class="abs login">
    <h3>Login</h3>
    <label style="top:57px">Username</label>
    <div class="field" style="top:58px"></div>
    <label style="top:81px">Password</label>
    <div class="field" style="top:84px"></div>
    <div class="abs btn login-btn">LOGIN</div>
  </div>

  <div class="abs photos-band"></div>
  <div class="abs photos-title">MY PHOTOS</div>
  <div class="abs photos-rule"></div>
  <div class="abs thumb thumb-nature" role="img" aria-label="Nature photograph of wildflowers in grass"></div>
  <div class="abs thumb thumb-scene" role="img" aria-label="Scenic photograph of a lake at dusk"></div>
  <div class="abs thumb thumb-wildlife" role="img" aria-label="Wildlife photograph of an insect on a grass blade"></div>
  <div class="abs thumb-label" style="left:186px">NATURE</div>
  <div class="abs thumb-label" style="left:394px">SCENE</div>
  <div class="abs thumb-label" style="left:599px">WILDLIFE</div>

  <footer class="abs footer">Copyright 2014&nbsp; Derek Holloway&nbsp; Contact Us&nbsp; |&nbsp; Terms and Conditions</footer>
</div>
</body>
</html>
```